BUSINESS CARD DESIGN

NAME- TODD MASVERIK
PHONE NUMER - 808- 451-7082
EMAIL- OFFICE@VORLINDE-GRADEWAY.COM
BACK OF CARD- SPEACIALIZES IN LAND CLEARING, FORESTRY MUCLHING AND EXCAVATION

Contact Information for Business Card

NAME- TODD MASVERIK PHONE NUMER - 808- 451-7082 EMAIL- OFFICE@VORLINDE-GRADEWAY.COM BACK OF CARD- SPEACIALIZES IN LAND CLEARING , MUCLHING AND EXCAVATION

```html
<!DOCTYPE html>
<html lang="en">
<head>
<meta charset="utf-8">
<title>Vorlinde Gradeway – Business Card</title>
<link href="https://fonts.googleapis.com/css2?family=Montserrat:wght@500;600;700;800&display=swap" rel="stylesheet">
<style>
  :root {
    --backdrop: #7b5e43;
    --card-front: #ffffff;
    --card-back: #0f0f0f;
    --ink: #111111;
    --accent: #f5b31c;
    --faint: #dadada;
    --pattern-dark: #1a1a1a;
    --pattern-light: #363636;
    --back-text: #bfbfbf;
  }
  * { margin: 0; padding: 0; box-sizing: border-box; }
  html, body { width: 900px; height: 1200px; overflow: hidden; }
  body {
    background: var(--backdrop);
    font-family: "Montserrat", sans-serif;
    position: relative;
  }
  .card {
    position: absolute;
    left: 80px;
    width: 742px;
    height: 440px;
    border-radius: 22px;
    overflow: hidden;
    box-shadow: 0 10px 24px rgba(0,0,0,.35);
  }
  .card-front { top: 132px; background: var(--card-front); }
  .card-back { top: 638px; background: var(--card-back); }

  /* Front */
  .brand {
    position: absolute;
    left: 52px;
    top: 40px;
    width: 240px;
    display: flex;
    flex-direction: column;
    align-items: center;
    gap: 12px;
  }
  .brand-dot {
    width: 96px; height: 96px;
    border-radius: 50%;
    background: var(--ink);
  }
  .brand-name {
    font-weight: 800;
    font-size: 21px;
    line-height: 1.15;
    color: var(--ink);
    letter-spacing: .5px;
    text-align: center;
  }
  .brand-phone {
    font-weight: 800;
    font-size: 13px;
    letter-spacing: 5px;
    color: var(--ink);
    margin-top: -6px;
  }

  .person {
    position: absolute;
    right: 32px;
    top: 38px;
    text-align: right;
  }
  .person-name {
    font-weight: 700;
    font-size: 25px;
    color: var(--accent);
    letter-spacing: .3px;
  }
  .person-role {
    font-weight: 500;
    font-size: 16px;
    color: var(--ink);
    margin-top: 4px;
  }

  .faint-name {
    position: absolute;
    left: 405px;
    top: 235px;
    width: 325px;
    font-weight: 800;
    font-size: 42px;
    line-height: 1.1;
    color: var(--faint);
    text-align: center;
  }

  .contacts {
    position: absolute;
    left: 42px;
    top: 320px;
    list-style: none;
  }
  .contacts li {
    display: flex;
    align-items: center;
    gap: 9px;
    height: 28px;
    font-weight: 500;
    font-size: 16px;
    color: var(--ink);
  }
  .contacts svg { width: 17px; height: 17px; flex: none; }

  /* Back */
  .back-pattern {
    position: absolute;
    inset: 0;
    background: radial-gradient(ellipse at 15% 30%, var(--pattern-light) 0%, var(--pattern-dark) 55%, var(--card-back) 100%);
  }
  .back-mark {
    position: absolute;
    left: 545px;
    top: 272px;
    display: flex;
    align-items: center;
    gap: 6px;
  }
  .back-mark-dot {
    width: 22px; height: 22px;
    border-radius: 50%;
    background: #ffffff;
  }
  .back-mark-name {
    font-weight: 800;
    font-size: 13px;
    line-height: 1.1;
    color: #ffffff;
  }
  .back-tagline {
    position: absolute;
    left: 0;
    right: 0;
    top: 392px;
    text-align: center;
    font-weight: 600;
    font-size: 12px;
    letter-spacing: 1.4px;
    color: var(--back-text);
  }
</style>
</head>
<body>

<section class="card card-front">
  <div class="brand">
    <span class="brand-dot"></span>
    <span class="brand-name">VORLINDE GRADEWAY LLC</span>
    <span class="brand-phone">808-451-7082</span>
  </div>

  <div class="person">
    <div class="person-name">TODD MASVERIK</div>
    <div class="person-role">Managing Director</div>
  </div>

  <div class="faint-name" aria-hidden="true">VORLINDE GRADEWAY</div>

  <ul class="contacts">
    <li>
      <svg viewBox="0 0 24 24" aria-hidden="true"><path fill="var(--accent)" d="M6.6 10.8a15.1 15.1 0 0 0 6.6 6.6l2.2-2.2a1 1 0 0 1 1-.25 11.4 11.4 0 0 0 3.6.57 1 1 0 0 1 1 1V20a1 1 0 0 1-1 1A17 17 0 0 1 3 4a1 1 0 0 1 1-1h3.5a1 1 0 0 1 1 1c0 1.25.2 2.45.57 3.57a1 1 0 0 1-.25 1z"/></svg>
      808- 451-7082
    </li>
    <li>
      <svg viewBox="0 0 24 24" aria-hidden="true"><rect x="2" y="5" width="20" height="14" rx="1.5" fill="var(--accent)"/><path d="M3 6l9 7 9-7" stroke="#fff" stroke-width="1.6" fill="none"/></svg>
      OFFICE@VORLINDE-GRADEWAY.COM
    </li>
    <li>
      <svg viewBox="0 0 24 24" aria-hidden="true"><circle cx="12" cy="12" r="10" fill="var(--accent)"/><path d="M2 12h20M12 2c3 3 3 17 0 20M12 2c-3 3-3 17 0 20" stroke="#fff" stroke-width="1.3" fill="none"/></svg>
      WWW.VORLINDE-GRADEWAY.COM
    </li>
  </ul>
</section>

<section class="card card-back">
  <div class="back-pattern" role="img" aria-label="Repeating tone-on-tone embossed company emblem pattern across a black card"></div>
  <div class="back-mark">
    <span class="back-mark-dot"></span>
    <span class="back-mark-name">VORLINDE<br>GRADEWAY</span>
  </div>
  <p class="back-tagline">SPECIALIZES IN LAND CLEARING, FORESTRY MULCHING AND EXCAVATION</p>
</section>

</body>
</html>
```